DOUBLE SIDED BROCHURE NEEDED TO PROMOTE DOCTOR

I need a double sided DL size (99mm x 210mm) brochure, promoting a doctor seeing patients in a new area.

I want something professional. I have included the relevant information. I would also like the Dr's picture somwhere in the brochure, with a professional background. I wish to print these tomorrow, so i will pick a winner within 14 hours of posting this ad.

I have included an example of a brochures design that I recently saw, and its definietly a good starting point.

Industry/Entity Type

Medical

```html
<!DOCTYPE html>
<html lang="en">
<head>
<meta charset="utf-8">
<title>Dr. Samir Haddad – DL Brochure</title>
<link href="https://fonts.googleapis.com/css2?family=Roboto+Slab:wght@700;800;900&family=Questrial&family=Nunito+Sans:ital,wght@1,900&family=Jost:ital,wght@0,400;1,400&display=swap" rel="stylesheet">
<style>
  :root {
    --backdrop: #5c5c5c;
    --blue-deep: #0a6fc4;
    --blue-bright: #0aa4e6;
    --blue-panel: #0b73cc;
    --yellow: #e2e64a;
    --ink: #111111;
    --heading-ink: #2b2b2b;
    --white: #ffffff;
    --black: #000000;
  }
  * { box-sizing: border-box; margin: 0; padding: 0; }
  html, body { width: 1200px; height: 1200px; overflow: hidden; }
  body { background: var(--backdrop); position: relative; font-family: "Questrial", sans-serif; }

  .panel { position: absolute; top: 58px; width: 522px; height: 1106px; background: var(--white); overflow: hidden; }
  .panel--front { left: 52px; }
  .panel--back { left: 622px; }

  /* Front */
  .portrait { position: absolute; left: 0; top: 0; width: 522px; height: 442px;
    background: linear-gradient(180deg, #8fb6e0 0%, #c9d7e6 45%, #5d5f66 75%, #2a2d38 100%); }
  .name-band { position: absolute; left: 0; top: 446px; width: 522px; height: 252px;
    background: linear-gradient(90deg, var(--blue-deep) 0%, var(--blue-bright) 100%); text-align: center; }
  .name-band__first { position: absolute; left: 0; right: 0; top: 56px; font-family: "Roboto Slab", serif; font-weight: 800;
    font-size: 56px; line-height: 1; color: var(--white); letter-spacing: -2px; }
  .name-band__last { position: absolute; left: 0; right: 0; top: 100px; font-family: "Roboto Slab", serif; font-weight: 800;
    font-size: 100px; line-height: 1; color: var(--yellow); letter-spacing: -4px; }
  .name-band__role { position: absolute; left: 0; right: 0; top: 218px; font-family: "Nunito Sans", sans-serif; font-style: italic;
    font-weight: 900; font-size: 25px; line-height: 1; color: var(--white); letter-spacing: -1px; }

  .letter { position: absolute; left: 60px; top: 718px; width: 458px; font-size: 23px; line-height: 29.5px; color: var(--ink); text-align: justify; }
  .letter__greeting { font-family: "Nunito Sans", sans-serif; font-style: italic; font-weight: 900; font-size: 21px; letter-spacing: -0.5px; }
  .letter p + p { margin-top: 29px; }
  .letter strong { font-weight: 700; -webkit-text-stroke: 0.6px var(--ink); }

  .contact-bar { position: absolute; left: 0; bottom: 0; width: 522px; height: 106px; background: var(--black); color: var(--white);
    font-family: "Jost", sans-serif; }
  .contact-bar__clinic { position: absolute; left: 38px; top: 30px; font-size: 16px; line-height: 21px; }
  .contact-bar__lines { position: absolute; right: 38px; top: 14px; text-align: right; font-size: 17px; line-height: 17px; }
  .contact-bar__label { font-style: italic; font-size: 14px; }
  .contact-bar__note { font-style: italic; font-size: 14px; margin-top: 6px; }

  /* Back */
  .theatre { position: absolute; left: 0; top: 0; width: 522px; height: 316px;
    background: linear-gradient(135deg, #5fb2d6 0%, #86c6e0 40%, #d7e4ea 70%, #3f9bc6 100%); }
  .intro { position: absolute; left: 0; top: 316px; width: 522px; height: 302px; background: var(--white); }
  .intro__name { position: absolute; left: 42px; top: 82px; font-family: "Roboto Slab", serif; font-weight: 800; font-size: 74px; line-height: 1;
    letter-spacing: -3px; background: linear-gradient(90deg, var(--blue-deep), var(--blue-bright));
    -webkit-background-clip: text; background-clip: text; color: transparent; }
  .intro__text { position: absolute; left: 45px; top: 158px; width: 434px; font-family: "Roboto Slab", serif; font-weight: 800;
    font-size: 20px; line-height: 30.5px; color: var(--heading-ink); text-align: justify; text-align-last: left; }

  .services { position: absolute; left: 0; top: 618px; width: 522px; height: 488px; background: var(--blue-panel); color: var(--white); }
  .services ul { list-style: none; position: absolute; left: 38px; width: 460px; }
  .services li { position: relative; padding-left: 45px; font-size: 24px; line-height: 31.8px; }
  .services li::before { content: ""; position: absolute; left: 2px; top: 12px; width: 9px; height: 9px; border-radius: 50%; background: var(--white); }
  .services li.no-bullet::before { display: none; }
  .services__primary { top: 27px; }
  .services__heading { position: absolute; left: 38px; top: 238px; font-family: "Roboto Slab", serif; font-weight: 800; font-size: 21px;
    line-height: 27px; text-decoration: underline; text-underline-offset: 2px; }
  .services__general { top: 308px; }
</style>
</head>
<body>
  <section class="panel panel--front">
    <div class="portrait" role="img" aria-label="Portrait photo of the surgeon in a jacket, modern building and sky behind"></div>
    <div class="name-band">
      <div class="name-band__first">DR. SAMIR</div>
      <div class="name-band__last">HADDAD</div>
      <div class="name-band__role">(General, Breast &amp; Endocrine Surgeon)</div>
    </div>
    <div class="letter">
      <p><span class="letter__greeting">Dear Doctors,</span><br>
      We are pleased to announce that <strong>Dr. Samir Haddad</strong> is now consulting in Coastvale, seeing public and private patients.</p>
      <p>Guaranteed appointment within two weeks, with patients having the option of surgery at Bayside Health Campus, Southgate General Hospital or St. Clare Hospital Riverton.</p>
    </div>
    <footer class="contact-bar">
      <div class="contact-bar__clinic">Coastvale Clinic:<br>42 Harbour View Road<br>Coastvale WA 6999.</div>
      <div class="contact-bar__lines">
        <div class="contact-bar__label">Phone:</div>
        <div>1300 000 123</div>
        <div class="contact-bar__note">Please send all referrals by fax to</div>
        <div>(08) 5550 1234.</div>
      </div>
    </footer>
  </section>

  <section class="panel panel--back">
    <div class="theatre" role="img" aria-label="Photo of a surgical team in blue scrubs operating in a theatre"></div>
    <div class="intro">
      <div class="intro__name">DR. HADDAD</div>
      <p class="intro__text">IS A HIGHLY TRAINED SPECIALISED SURGEON, IN ALL AREAS OF ENDOCRINE, BREAST AND GENERAL SURGERY. INCLUDING;</p>
    </div>
    <div class="services">
      <ul class="services__primary">
        <li>Thyroid Surgery</li>
        <li>Parathyroid surgery (including minimally invasive parathyroidectomy)</li>
        <li>Breast Cancer</li>
        <li class="no-bullet">Benign breast lesions</li>
      </ul>
      <div class="services__heading">ALL AREAS OF GENERAL SURGERY,<br>SUCH AS;</div>
      <ul class="services__general">
        <li>Gallbladder surgery</li>
        <li>Hernia surgery</li>
        <li>Haemorrhoids</li>
        <li>Carpal Tunnel</li>
        <li>Vasectomy etc etc…</li>
      </ul>
    </div>
  </section>
</body>
</html>
```